依頼詳細
・サイズ:
シート看板 1800×6000(縦でも横でも可)
(建築現場での広告のため車で前面道路を通っても伝わるようなデザイン)

キャッチコピーとしては「建築相談受付中」や「土地活用無料相談」などのアパート建築に係る内容を検討して頂ければと思います。
記載項目
会社名/ヒサノホーム株式会社
電話番号/098-631-2947
(ロゴを添付)
希望イメージ
シンプル 複雑
単色 カラフル
暗い 明るい
日常 高級
遊び心 厳粛
未来的 伝統的
女性的 男性的
希望する色
赤系、黄・オレンジ系、緑系
補足説明
まずはデザインを出していただき、詳細はデザイン決定後
打ち合わせをしながら進めさせて頂きたいです。

その他ご質問等ありましたら、気軽にお問い合わせください。
ご応募をお待ちしております!

シンプルでイメージに合った提案だった。修正対応も迅速で丁寧に対応して頂いた。

今回はご提案き誠にありがとうございました。今後も広告等のデザイン作成依頼を予定しておりますのでご参加いただけると幸いです。

```html
<!DOCTYPE html>
<html lang="ja">
<head>
<meta charset="utf-8">
<title>ヒサノホーム 建築相談 シート看板</title>
<link rel="stylesheet" href="https://fonts.googleapis.com/css2?family=Noto+Sans+JP:wght@500;700;900&display=swap">
<style>
  :root {
    --sky: #a9d9f2;
    --sky-deep: #8ccbeb;
    --banner: #3aa3de;
    --box: #2e9ee0;
    --ink: #111111;
    --white: #ffffff;
  }
  html, body { margin: 0; padding: 0; overflow: hidden; }
  body { width: 1200px; height: 4008px; }
  .sign {
    position: relative;
    width: 1200px;
    height: 4008px;
    overflow: hidden;
    background: var(--white);
    font-family: "Noto Sans JP", sans-serif;
  }
  .cityscape {
    position: absolute;
    left: 0; top: 0;
    width: 1200px; height: 3310px;
    background: linear-gradient(180deg, var(--sky) 0%, var(--sky-deep) 55%, var(--sky) 100%);
  }
  .target-banner {
    position: absolute;
    left: 36px; top: 0;
    width: 1128px; height: 740px;
    background: var(--banner);
    border-radius: 0 0 70px 70px;
    color: var(--white);
    text-align: center;
    font-weight: 700;
    font-size: 68px;
    line-height: 1.28;
  }
  .target-banner p { margin: 0; }
  .target-first { padding-top: 130px; }
  .target-divider {
    width: 1040px; height: 6px;
    margin: 32px auto 30px;
    background: var(--white);
  }
  .headline {
    position: absolute;
    top: 790px;
    display: flex;
    flex-direction: column;
    font-weight: 900;
    font-size: 400px;
    line-height: 385px;
    color: var(--ink);
    letter-spacing: 0;
  }
  .headline span { display: block; }
  .headline-building { left: 630px; }
  .headline-land { left: 80px; }
  .free-badge {
    position: absolute;
    top: 2385px;
    display: flex;
    flex-direction: column;
    gap: 14px;
  }
  .free-badge span {
    display: flex;
    align-items: center;
    justify-content: center;
    width: 410px; height: 410px;
    background: var(--box);
    box-shadow: inset 0 0 0 10px var(--sky);
    color: var(--white);
    font-weight: 900;
    font-size: 330px;
    line-height: 1;
  }
  .free-badge-consult { left: 636px; }
  .free-badge-free { left: 120px; }
  .contact {
    position: absolute;
    left: 0; top: 3310px;
    width: 1200px; height: 698px;
    background: var(--white);
    color: var(--ink);
  }
  .brand {
    position: absolute;
    left: 60px; top: 150px;
    display: flex; align-items: center; gap: 40px;
  }
  .brand-mark {
    width: 150px; height: 150px;
    border-radius: 50%;
    background: var(--ink);
  }
  .brand-name {
    font-weight: 500;
    font-size: 126px;
    letter-spacing: 6px;
    line-height: 1;
  }
  .tel {
    position: absolute;
    left: 90px; top: 390px;
    font-weight: 700;
    font-size: 90px;
    line-height: 1;
  }
  .tel small { font-size: 62px; margin-right: 20px; }
  .url {
    position: absolute;
    left: 0; top: 550px; width: 1200px;
    text-align: center;
    font-weight: 500;
    font-size: 54px;
    line-height: 1;
  }
</style>
</head>
<body>
<div class="sign">
  <div class="cityscape" role="img" aria-label="淡いブルーの線画で描かれた俯瞰の街並み・ビル群のイラスト"></div>

  <div class="target-banner">
    <p class="target-first">築古の住宅・アパートの<br>建て替えを検討している方</p>
    <div class="target-divider"></div>
    <p>アパート建築用地をお持ちの<br>地主様・相続予定者様</p>
  </div>

  <div class="headline headline-building"><span>建</span><span>築</span><span>相</span><span>談</span></div>
  <div class="headline headline-land"><span>土</span><span>地</span><span>活</span><span>用</span></div>

  <div class="free-badge free-badge-consult"><span>相</span><span>談</span></div>
  <div class="free-badge free-badge-free"><span>無</span><span>料</span></div>

  <div class="contact">
    <div class="brand">
      <div class="brand-mark"></div>
      <div class="brand-name">HISANO HOME</div>
    </div>
    <div class="tel"><small>TEL</small>098-631-2947</div>
    <div class="url">https://www.hisano-home.co.jp/build/</div>
  </div>
</div>
</body>
</html>
```